Reid Calloway Fitness Business Card

I Need a really cool and creative yet modern and cutting edge. I run a personal training company, I have a logo already which ill submit images of. Id like the base colors to be black and white with a little red as a highlight color. Charcoal grey is fine also. My clientele is mostly comprised of young professionals who are in touch with modern culture art and are interested in "cool" so if there was one thing i want this business card to be it sexy and cool.

Target Market(s)

young professionals who are image conscious, care about their health, looking and feeling good. They know what is cool and expect the best.

Industry/Entity Type

Training

Requirements
Must have
• - must be a 2 sided card
- must include the following:

Reid Calloway CPT
604 392 7715
Reid@ReidCallowayFitness.example
www.ReidCallowayFitness.example
Nice to have
• id like to see some unconventional shape ideas as well as conventional ones

```html
<!DOCTYPE html>
<html lang="en">
<head>
<meta charset="utf-8">
<title>Reid Calloway Fitness — Business Card</title>
<link rel="stylesheet" href="https://fonts.googleapis.com/css2?family=EB+Garamond:wght@400;500&display=swap">
<style>
  :root {
    --ink: #0b0b0b;
    --paper: #ffffff;
    --accent: #d71f26;
    --text: #2a2a2a;
    --backdrop: #e6e4e1;
  }
  * { margin: 0; padding: 0; box-sizing: border-box; }
  html, body {
    width: 1064px;
    height: 1200px;
    overflow: hidden;
    background: var(--backdrop);
    font-family: "EB Garamond", Garamond, Georgia, serif;
  }
  .canvas {
    position: relative;
    width: 1064px;
    height: 1200px;
  }
  .card {
    position: absolute;
    left: 82px;
    width: 900px;
    height: 514px;
    overflow: hidden;
    border: 2px solid #111;
    box-shadow: 0 4px 14px rgba(0,0,0,0.18);
  }
  .card--front { top: 62px; background: var(--paper); }
  .card--back { top: 624px; background: var(--ink); }

  /* Front side */
  .front__mark-panel {
    position: absolute;
    left: 0; top: 0; bottom: 0;
    width: 412px;
    background: var(--ink);
  }
  .front__rule {
    position: absolute;
    top: 0; bottom: 0;
    left: 420px;
    width: 8px;
    background: var(--accent);
  }
  .brand {
    position: absolute;
    display: flex;
    align-items: center;
    gap: 16px;
    color: var(--paper);
    font-weight: 500;
    line-height: 1.05;
  }
  .brand__square {
    width: 22px;
    height: 22px;
    background: var(--accent);
    flex: none;
  }
  .front__mark-panel .brand {
    left: 48px;
    top: 190px;
    font-size: 40px;
  }
  .identity {
    position: absolute;
    left: 480px;
    top: 84px;
  }
  .identity__name {
    color: var(--accent);
    font-size: 38px;
    font-weight: 500;
    font-variant: small-caps;
    letter-spacing: 0.5px;
    line-height: 1;
  }
  .identity__title {
    color: var(--text);
    font-size: 27px;
    font-weight: 500;
    letter-spacing: 1px;
    line-height: 1.1;
  }
  .contact {
    position: absolute;
    left: 480px;
    top: 316px;
    list-style: none;
    color: var(--text);
    font-size: 23px;
    line-height: 38px;
  }

  /* Back side */
  .back__strip {
    position: absolute;
    top: 0; bottom: 0; right: 0;
    width: 146px;
    background: var(--paper);
  }
  .back__rule {
    position: absolute;
    top: 0; bottom: 0;
    left: 34px;
    width: 10px;
    background: var(--accent);
  }
  .card--back .brand {
    left: 70px;
    top: 150px;
    font-size: 60px;
  }
  .back__url {
    position: absolute;
    right: 190px;
    bottom: 72px;
    color: var(--paper);
    font-size: 30px;
    font-weight: 500;
  }
</style>
</head>
<body>
<main class="canvas">

  <section class="card card--front" aria-label="Card front">
    <div class="front__mark-panel">
      <div class="brand">
        <span class="brand__square"></span>
        <span class="brand__name">Reid Calloway<br>Fitness</span>
      </div>
    </div>
    <div class="front__rule"></div>
    <div class="identity">
      <h1 class="identity__name">Reid Calloway</h1>
      <p class="identity__title">CPT</p>
    </div>
    <ul class="contact">
      <li>604 392 7715</li>
      <li>Reid@ReidCallowayFitness.example</li>
      <li>www.ReidCallowayFitness.example</li>
    </ul>
  </section>

  <section class="card card--back" aria-label="Card back">
    <div class="brand">
      <span class="brand__square"></span>
      <span class="brand__name">Reid Calloway<br>Fitness</span>
    </div>
    <p class="back__url">www.ReidCallowayFitness.example</p>
    <div class="back__strip">
      <div class="back__rule"></div>
    </div>
  </section>

</main>
</body>
</html>
```